Business Card Design using new logo

As much as we'd like to think that treating everyone equally is the best strategy for fairness, the reality is that the differences in the lives of women and men have to be taken into account to ensure that organizations, programs, services, and yes, even public policy treat women and men in ways that achieve gender equity.

That's where ParityLumen - fairness metrics insight comes in. Using the data-driven tools of gender analysis, our organization can help anyone determine if gender equity is being achieved - in businesses and organizations, in the planning and implementation of programs and services, and in the development and enforcement of public policy.
Updates

Apologies for the delay - have not had time to finalize the decision.  Should be early this week - probably Tuesday.

Industry/Entity Type

Business

Requirements
Must have
• New Logo for ParityLumen
• Logo plus words "Fairness Metrics Insight"

```html
<!DOCTYPE html>
<html lang="en">
<head>
<meta charset="utf-8">
<title>ParityLumen Business Cards</title>
<link rel="stylesheet" href="https://fonts.googleapis.com/css2?family=Exo+2:wght@500&family=Ubuntu:wght@400;500&display=swap">
<style>
  :root {
    --stage: #1d1d1d;
    --card-dark: #333333;
    --card-light: #ffffff;
    --orange: #f7941d;
    --silver: #c4c4c4;
    --ink: #222222;
    --rule: #9a9a9a;
  }
  * { margin: 0; padding: 0; box-sizing: border-box; }
  html, body { width: 1200px; height: 900px; overflow: hidden; }
  body {
    background: var(--stage);
    position: relative;
    font-family: "Ubuntu", Arial, sans-serif;
  }
  .card {
    position: absolute;
    width: 472px;
    height: 269px;
    overflow: hidden;
  }
  .card--front { left: 94px; top: 191px; background: var(--card-dark); }
  .card--back { left: 593px; background: var(--card-light); }
  .card--ceo { top: 191px; }
  .card--cgo { top: 489px; }

  .brand-dot {
    position: absolute;
    border-radius: 50%;
    background: var(--orange);
  }
  .wordmark {
    position: absolute;
    font-family: "Exo 2", Arial, sans-serif;
    font-weight: 500;
    white-space: nowrap;
    line-height: 1;
  }
  .card--front .brand-dot { left: 206px; top: 62px; width: 60px; height: 60px; }
  .card--front .wordmark {
    left: 0; width: 472px; text-align: center;
    top: 150px; font-size: 42px; color: var(--silver);
  }
  .tagline {
    position: absolute; left: 0; width: 472px; text-align: center;
    top: 203px; font-size: 14.5px; color: var(--orange); letter-spacing: 0.3px;
  }
  .front-bar {
    position: absolute; left: 50px; right: 0; top: 235px; height: 12px;
    background: var(--silver);
  }

  .card--back .brand-dot { left: 38px; top: 44px; width: 52px; height: 52px; }
  .card--back .wordmark { left: 104px; top: 53px; font-size: 34px; color: var(--ink); }

  .holder { position: absolute; left: 46px; top: 126px; }
  .holder-name { font-size: 14px; font-weight: 500; color: var(--ink); line-height: 16px; }
  .holder-title { font-size: 10px; color: var(--orange); line-height: 12px; }

  .contact { position: absolute; font-size: 10.5px; line-height: 12.6px; color: var(--ink); }
  .contact--main { left: 46px; top: 162px; }
  .contact--office {
    left: 260px; top: 175px; padding-left: 7px;
    border-left: 1px solid var(--rule);
  }
  .label { color: var(--orange); }
  .web { color: var(--orange); }

  .arrow { position: absolute; left: 0; top: 225px; width: 430px; height: 34px; }
</style>
</head>
<body>

<section class="card card--front" aria-label="Card front">
  <span class="brand-dot"></span>
  <p class="wordmark">ParityLumen</p>
  <p class="tagline">Fairness Metrics Insight</p>
  <span class="front-bar"></span>
</section>

<section class="card card--back card--ceo" aria-label="Card back, Marin Holloway">
  <span class="brand-dot"></span>
  <p class="wordmark">ParityLumen</p>
  <div class="holder">
    <p class="holder-name">Marin Holloway</p>
    <p class="holder-title">CEO</p>
  </div>
  <div class="contact contact--main">
    <p>Fairness Metrics Insight LLC</p>
    <p><span class="label">C:</span> 555-210-4831</p>
    <p><span class="label">E:</span> mholloway@paritylumen.com</p>
    <p><span class="label">T:</span> @ParityLumen</p>
  </div>
  <div class="contact contact--office">
    <p><span class="label">O:</span> 555-018-2240</p>
    <p><span class="label">F:</span> 800-555-0147</p>
    <p class="web">ParityLumen.com</p>
  </div>
  <svg class="arrow" viewBox="0 0 430 34" aria-hidden="true">
    <polygon points="0,11 408,11 408,0 427,17 408,34 408,23 0,23" fill="var(--orange)"/>
  </svg>
</section>

<section class="card card--back card--cgo" aria-label="Card back, Theo Castell">
  <span class="brand-dot"></span>
  <p class="wordmark">ParityLumen</p>
  <div class="holder">
    <p class="holder-name">Theo Castell</p>
    <p class="holder-title">CGO</p>
  </div>
  <div class="contact contact--main">
    <p>Fairness Metrics Insight LLC</p>
    <p><span class="label">C:</span> 555-374-9026</p>
    <p><span class="label">E:</span> tcastell@paritylumen.com</p>
    <p><span class="label">T:</span> @tcastell</p>
  </div>
  <div class="contact contact--office">
    <p><span class="label">O:</span> 555-018-2240</p>
    <p><span class="label">F:</span> 800-555-0147</p>
    <p class="web">ParityLumen.com</p>
  </div>
  <svg class="arrow" viewBox="0 0 430 34" aria-hidden="true">
    <polygon points="0,11 408,11 408,0 427,17 408,34 408,23 0,23" fill="var(--orange)"/>
  </svg>
</section>

</body>
</html>
```